PowerPoint Template Briefing for VARDUL

Create a professional, consistent PowerPoint template in 16:9 format that adheres to VARDUL's corporate identity guidelines. This template will be used regularly for client presentations, project proposals, and internal communications.

Template Requirements
- Format: 16:9 widescreen format for modern display compatibility
- Master slides to include:
- - Title slide with prominent logo placement
- - Section divider slides
- - Content slides with various layouts (text only, text with images, comparison layouts)
- - Data presentation slides (charts, tables, graphs)
- - Quote/testimonial slide
- - Contact/closing slide

Brand Elements Integration
- Logo placement: Consistent positioning on all slides (preferably top left or bottom right)
- Use both logo variations appropriately (text under icon for title slides, text right of icon for content slides)
- Color scheme: Implement the VARDUL color palette throughout:
- - Primary Dark Gray (#404040) for main text and headers
- - Primary Blue (#295F7C) for accents and highlights
- - Highlight Blue (#3B8AB4) for call-outs and emphasis
- Typography: Montserrat font family exclusively, with appropriate size hierarchy:
- - Slide titles: Montserrat Bold
- - Headings: Montserrat SemiBold
- - Body text: Montserrat Regular
- - Captions/footnotes: Montserrat Light

Design Elements
- Clean, minimalist design with ample white space
- Subtle background elements that evoke global connectivity and time zones
- Modern, professional look aligned with IT industry standards
- Consistent footer with slide numbers and optional space for confidentiality notices
- Custom bullet points and dividers using brand colors

Technical Specifications
- Compatible with PowerPoint 2016 and newer versions
- Embedded Montserrat font or fallback instructions
- Editable text boxes and image placeholders
- Properly set up slide masters and layouts
- Optimized file size for easy sharing

Deliverables
- .POTX template file
- Brief usage guidelines for the template
- Sample slides demonstrating various layouts and proper usage

This template should serve as the foundation for all VARDUL presentations, ensuring brand consistency while providing flexibility for various content needs.undefined

```html
<!DOCTYPE html>
<html lang="en">
<head>
<meta charset="utf-8">
<title>VARDUL – Presentation Template Overview</title>
<link href="https://fonts.googleapis.com/css2?family=Montserrat:ital,wght@0,300;0,400;0,500;0,600;0,700;1,500&display=swap" rel="stylesheet">
<style>
  :root{
    --page-bg:#e6eaf1;
    --slide-bg:#ffffff;
    --ink:#333333;
    --text:#404040;
    --blue:#214a6b;
    --blue-bright:#3b8ab4;
    --bar-blue:#253d5c;
    --rule-grey:#c9c9c9;
    --soft-grey:#e4e8ee;
  }
  *{box-sizing:border-box;margin:0;padding:0}
  html,body{width:1028px;height:1200px;overflow:hidden;background:var(--page-bg)}
  body{position:relative;font-family:"Montserrat",sans-serif;color:var(--text)}

  .slide{position:absolute;width:455px;height:255px;background:var(--slide-bg);overflow:hidden;box-shadow:0 2px 8px rgba(40,55,80,.12)}
  .slide--title{left:39px;top:35px}
  .slide--about{left:533px;top:35px}
  .slide--break{left:39px;top:326px}
  .slide--services{left:537px;top:326px}
  .slide--team{left:39px;top:617px}
  .slide--testimonial{left:533px;top:617px}
  .slide--chart{left:39px;top:907px}
  .slide--contact{left:537px;top:907px}

  .footer{position:absolute;left:0;bottom:0;width:455px;height:22px}
  .footer svg{position:absolute;inset:0}
  .footer-date,.footer-page{position:absolute;font-size:5.6px;font-weight:500;color:#fff}
  .footer-date{left:23px;bottom:4px}
  .footer-page{right:23px;bottom:6px}

  .slide-title{position:absolute;left:23px;top:11px;font-size:14.5px;font-weight:700;color:var(--ink);letter-spacing:.2px;line-height:1}
  .slide-title .accent{color:var(--blue)}
  .title-mark{position:absolute;left:23px;top:30px;width:17px;height:3px}
  .title-mark::before{content:"";position:absolute;left:0;top:0;width:3px;height:3px;border-radius:50%;background:var(--ink)}
  .title-mark::after{content:"";position:absolute;left:6px;top:0;width:11px;height:3px;border-radius:2px;background:var(--blue)}

  .brand{position:absolute;right:23px;top:16px;display:flex;align-items:center;gap:4px}
  .brand-dot{width:12px;height:12px;border-radius:50%;border:2px solid var(--ink)}
  .brand-name{font-size:14.5px;font-weight:600;color:var(--blue);letter-spacing:.3px;line-height:1}

  .hero-wave{position:absolute;inset:0}
  .hero-heading{position:absolute;left:23px;top:28px;font-size:15.3px;font-weight:700;color:#fff;line-height:22.5px;letter-spacing:.3px}
  .hero-sub{position:absolute;left:23px;top:101px;font-size:6.2px;font-weight:500;color:#fff;line-height:14px}
  .hero-photo-ring{position:absolute;left:231px;top:20px;width:210px;height:210px;border-radius:50%;border:2px solid #fff;background:#2b2b2b;box-shadow:0 0 0 1px rgba(0,0,0,.2)}
  .hero-photo{position:absolute;left:240px;top:29px;width:192px;height:192px;border-radius:50%;background:radial-gradient(circle at 50% 35%,#7fa8d0 0%,#2d4e72 38%,#16263a 70%,#0c121b 100%)}
  .hero-brand{position:absolute;left:23px;top:196px;font-size:23px;font-weight:600;color:var(--blue);letter-spacing:.5px}
  .hero-brand-dot{position:absolute;left:53px;top:151px;width:40px;height:40px;border-radius:50%;border:5px solid var(--ink)}
  .hero-baseline{position:absolute;left:0;bottom:0;width:455px;height:2.5px;background:var(--blue)}

  .about-col{position:absolute;top:60px;width:189px;font-size:5.6px;line-height:10.6px;text-align:justify;color:var(--text)}
  .about-col p+p{margin-top:10.6px}
  .about-col--left{left:23px}
  .about-col--right{left:243px}

  .break-ring{position:absolute;left:142px;top:29px;width:180px;height:180px;border-radius:50%;border:12px solid var(--ink)}
  .break-title{position:absolute;left:0;width:455px;top:100px;text-align:center;font-size:33px;font-weight:700;color:var(--blue);letter-spacing:.5px;line-height:1}

  .service{position:absolute;width:130px;text-align:center}
  .service-ring{position:absolute;width:90px;height:90px;border-radius:50%;border:5px solid var(--ink);background:#fff}
  .service-photo{position:absolute;left:5px;top:5px;width:70px;height:70px;border-radius:50%}
  .service-name{position:absolute;left:0;width:130px;font-size:6.3px;font-weight:600;line-height:10.6px;color:var(--ink)}
  .service-desc{position:absolute;left:0;width:130px;font-size:5.7px;font-weight:400;line-height:10.6px;color:var(--text)}

  .founder-name{position:absolute;left:23px;top:58px;font-size:10px;font-weight:600;color:var(--blue)}
  .founder-bio{position:absolute;left:23px;top:72px;width:234px;font-size:5.6px;line-height:10.6px;text-align:justify}
  .founder-bio p+p{margin-top:10.6px}
  .portrait-ring{position:absolute;left:288px;top:68px;width:144px;height:144px;border-radius:50%;border:12px solid var(--ink)}
  .portrait{position:absolute;left:304px;top:84px;width:112px;height:112px;border-radius:50%;border:2px solid #fff;background:linear-gradient(180deg,#4a4a4a 0%,#5a5a5a 45%,#2a3550 75%,#1c2740 100%)}

  .quote-card{position:absolute;left:64px;top:72px;width:327px;height:114px;border-radius:8px;background:var(--ink);text-align:center;color:#fff}
  .quote-mark{position:absolute;left:0;width:455px;top:52px;text-align:center;font-size:64px;font-weight:700;color:var(--blue);line-height:1;height:26px;overflow:hidden}
  .quote-text{position:absolute;left:14px;top:25px;width:299px;font-size:8.6px;font-weight:500;line-height:16.6px}
  .quote-author{position:absolute;left:0;width:327px;top:87px;font-size:8.6px;font-style:italic;font-weight:500}

  .stat{position:absolute;text-align:center;width:60px}
  .stat-value{font-size:17px;font-weight:500;color:var(--ink);line-height:1}
  .stat-label{font-size:6.8px;font-weight:500;color:var(--ink);margin-top:5px}
  .stat-label--blue{color:var(--blue)}
  .chart{position:absolute;left:110px;top:60px;width:250px;height:115px}
  .chart-caption{position:absolute;left:113px;top:185px;width:210px;font-size:6.6px;line-height:14px;color:var(--ink)}
  .chart-notes{position:absolute;left:344px;top:63px;width:87px;font-size:6.6px;line-height:11.8px;text-align:justify;color:var(--ink)}
  .chart-notes p+p{margin-top:11.8px}

  .contact-brand{position:absolute;left:132px;top:60px;display:flex;align-items:center;gap:10px}
  .contact-brand-dot{width:44px;height:44px;border-radius:50%;border:5px solid var(--ink)}
  .contact-brand-name{font-size:32px;font-weight:600;color:var(--blue);letter-spacing:.6px;line-height:1}
  .contact-item{position:absolute;top:124px;display:flex;gap:8px}
  .contact-icon{width:20px;height:20px;border-radius:50%;background:var(--ink);display:flex;align-items:center;justify-content:center;margin-top:3px;flex:none}
  .contact-label{font-size:6.5px;font-weight:600;color:var(--blue);line-height:9px}
  .contact-value{font-size:8px;font-weight:500;color:var(--ink);line-height:13px;margin-top:1px}
  .thank-you{position:absolute;left:0;width:455px;top:172px;text-align:center;font-size:17.5px;font-weight:600;color:var(--ink);letter-spacing:.4px}
  .contact-watermark{position:absolute;left:141px;top:34px;width:174px;height:174px;border-radius:50%;border:10px solid #f1f2f4}
</style>
</head>
<body>

<section class="slide slide--title">
  <svg class="hero-wave" viewBox="0 0 455 255" width="455" height="255" aria-hidden="true">
    <path d="M0 0 H455 V88 C395 92 335 108 265 132 C175 162 85 172 0 154 Z" fill="#2f2f2f"/>
  </svg>
  <div class="hero-photo-ring"></div>
  <div class="hero-photo" role="img" aria-label="Businessman seen from behind facing a large screen with a glowing globe and data grid"></div>
  <h1 class="hero-heading">SMART IT OUTSOURCING<br>&amp; SCALABLE BUSINESS<br>GROWTH</h1>
  <p class="hero-sub">Optimize costs, enhance flexibility and execute IT Projects<br>with precision - globally and efficiently</p>
  <div class="hero-brand-dot"></div>
  <div class="hero-brand">VARDUL</div>
  <div class="hero-baseline"></div>
</section>

<section class="slide slide--about">
  <h2 class="slide-title">ABOUT <span class="accent">VARDUL</span></h2>
  <div class="title-mark"></div>
  <div class="brand"><span class="brand-dot"></span><span class="brand-name">VARDUL</span></div>
  <div class="about-col about-col--left">
    <p>VARDUL is a forward-thinking IT services company specializing in connecting businesses with top-tier freelance experts and orchestrating offshore IT solutions. With a strong focus on agility, flexibility, and global collaboration, we empower companies to execute IT projects efficiently by leveraging a worldwide talent pool. Our unique approach ensures that businesses benefit from high-quality expertise while optimizing costs and delivery speed.</p>
    <p>The name VARDUL stands for vigilance around the clock, symbolizing our core strength—harnessing the time zone advantages of professionals in Australia and New Zealand to provide seamless support for European clients, even overnight. At VARDUL, we bridge geographical and operational gaps, ensuring companies receive the right expertise at the right time.</p>
  </div>
  <div class="about-col about-col--right">
    <p>Marten’s career spans leadership roles in both traditional and agile environments. Over the past 14 years, he has helped numerous clients transform into agile enterprises, implementing methodologies such as Kanban, Scrum, Lean Portfolio, and OKRs. His hands-on approach, combined with strategic vision, bridges business needs and IT execution.</p>
    <p>With extensive expertise in IT service management and project execution, Marten has successfully guided businesses in setting up, outsourcing, and managing IT projects. His deep understanding of both client and provider perspectives ensures seamless collaboration and optimal project outcomes. VARDUL reflects his dedication to innovation, agility, and global connectivity—helping businesses thrive in a rapidly evolving digital landscape.</p>
  </div>
  <div class="footer">
    <svg viewBox="0 0 455 22" width="455" height="22" aria-hidden="true">
      <rect x="0" y="1" width="300" height="3" fill="var(--rule-grey)"/>
      <rect x="0" y="3" width="455" height="19" fill="var(--ink)"/>
      <path d="M278 22 C285 8 296 1 318 1 H455 V22 Z" fill="#d4d4d4"/>
      <path d="M283 22 C290 9 301 2 322 2 H455 V22 Z" fill="var(--blue)"/>
    </svg>
    <span class="footer-date">12 May 2025</span><span class="footer-page">Page no: 02</span>
  </div>
</section>

<section class="slide slide--break">
  <div class="break-ring"></div>
  <h2 class="break-title">BREAK SLIDE</h2>
  <div class="footer">
    <svg viewBox="0 0 455 22" width="455" height="22" aria-hidden="true">
      <rect x="0" y="1" width="300" height="3" fill="var(--rule-grey)"/>
      <rect x="0" y="3" width="455" height="19" fill="var(--ink)"/>
      <path d="M278 22 C285 8 296 1 318 1 H455 V22 Z" fill="#d4d4d4"/>
      <path d="M283 22 C290 9 301 2 322 2 H455 V22 Z" fill="var(--blue)"/>
    </svg>
    <span class="footer-date">12 May 2025</span><span class="footer-page">Page no: 03</span>
  </div>
</section>

<section class="slide slide--services">
  <h2 class="slide-title">OUR <span class="accent">SERVICES</span></h2>
  <div class="title-mark"></div>
  <div class="brand"><span class="brand-dot"></span><span class="brand-name">VARDUL</span></div>

  <div class="service" style="left:22px;top:56px">
    <div class="service-ring" style="left:20px;top:0">
      <div class="service-photo" role="img" aria-label="Specialist touching a glowing digital globe interface" style="background:radial-gradient(circle at 40% 45%,#6fa9e0,#1f4f85 55%,#0f2440)"></div>
    </div>
    <p class="service-name" style="top:101px">Expert Matching –<br>Freelance IT Specialists</p>
    <p class="service-desc" style="top:130px">We connect businesses with experienced<br>IT professionals worldwide.</p>
  </div>

  <div class="service" style="left:163px;top:63px">
    <div class="service-ring" style="left:20px;top:0">
      <div class="service-photo" role="img" aria-label="Team in a video conference around a large screen" style="background:radial-gradient(circle at 50% 40%,#8fa6bf,#4a5e74 55%,#2a3442)"></div>
    </div>
    <p class="service-name" style="top:101px">Solution Orchestration –<br>Rent a Team</p>
    <p class="service-desc" style="top:130px">We integrate individual IT services and<br>providers into a fully functional.</p>
  </div>

  <div class="service" style="left:307px;top:56px">
    <div class="service-ring" style="left:20px;top:0">
      <div class="service-photo" role="img" aria-label="Screen showing agile, scrum and kanban dashboards" style="background:radial-gradient(circle at 50% 45%,#a9bcd0,#4d6680 55%,#1e2c3c)"></div>
    </div>
    <p class="service-name" style="top:101px">IT Consulting –<br>Agile &amp; Strategic Guidance</p>
    <p class="service-desc" style="top:130px">With over two decades of IT project<br>leadership, we offer expert consulting</p>
  </div>

  <div class="footer">
    <svg viewBox="0 0 455 22" width="455" height="22" aria-hidden="true">
      <rect x="0" y="1" width="300" height="3" fill="var(--rule-grey)"/>
      <rect x="0" y="3" width="455" height="19" fill="var(--ink)"/>
      <path d="M278 22 C285 8 296 1 318 1 H455 V22 Z" fill="#d4d4d4"/>
      <path d="M283 22 C290 9 301 2 322 2 H455 V22 Z" fill="var(--blue)"/>
    </svg>
    <span class="footer-date">12 May 2025</span><span class="footer-page">Page no: 04</span>
  </div>
</section>

<section class="slide slide--team">
  <h2 class="slide-title">MEET OUR <span class="accent">TEAM</span></h2>
  <div class="title-mark"></div>
  <div class="brand"><span class="brand-dot"></span><span class="brand-name">VARDUL</span></div>
  <h3 class="founder-name">Meet the Founder – Marten Kessel</h3>
  <div class="founder-bio">
    <p>Marten’s career spans leadership roles in both traditional and agile environments. Over the past 14 years, he has helped numerous clients transform into agile enterprises, implementing methodologies such as Kanban, Scrum, Lean Portfolio, and OKRs. His hands-on approach, combined with strategic vision, allows him to bridge the gap between business needs and IT execution effectively.</p>
    <p>With extensive expertise in IT service management and project execution, Marten has successfully guided businesses in setting up, outsourcing, and managing IT projects. His deep understanding of both client and service provider perspectives ensures seamless collaboration and optimal project outcomes. VARDUL reflects Marten’s dedication to innovation, agility, and global connectivity—helping businesses thrive in a rapidly evolving digital landscape.</p>
  </div>
  <div class="portrait-ring"></div>
  <div class="portrait" role="img" aria-label="Portrait photo of the founder in a dark blazer"></div>
  <div class="footer">
    <svg viewBox="0 0 455 22" width="455" height="22" aria-hidden="true">
      <rect x="0" y="1" width="300" height="3" fill="var(--rule-grey)"/>
      <rect x="0" y="3" width="455" height="19" fill="var(--ink)"/>
      <path d="M278 22 C285 8 296 1 318 1 H455 V22 Z" fill="#d4d4d4"/>
      <path d="M283 22 C290 9 301 2 322 2 H455 V22 Z" fill="var(--blue)"/>
    </svg>
    <span class="footer-date">12 May 2025</span><span class="footer-page">Page no: 05</span>
  </div>
</section>

<section class="slide slide--testimonial">
  <h2 class="slide-title">CLIENT <span class="accent">TESTIMONIALS</span></h2>
  <div class="title-mark"></div>
  <div class="brand"><span class="brand-dot"></span><span class="brand-name">VARDUL</span></div>
  <div class="quote-card">
    <p class="quote-text">Lorem ipsum dolor sit amet, consectetur adipiscing elit, sed do eiusmod tempor incididunt ut labore et dolore magna aliqua. Ut exercitation ullam ut aliquip ex ea commodo consequat.</p>
    <p class="quote-author">- SARAH LOREM</p>
  </div>
  <div class="quote-mark" aria-hidden="true">“</div>
  <div class="footer">
    <svg viewBox="0 0 455 22" width="455" height="22" aria-hidden="true">
      <rect x="0" y="1" width="300" height="3" fill="var(--rule-grey)"/>
      <rect x="0" y="3" width="455" height="19" fill="var(--ink)"/>
      <path d="M278 22 C285 8 296 1 318 1 H455 V22 Z" fill="#d4d4d4"/>
      <path d="M283 22 C290 9 301 2 322 2 H455 V22 Z" fill="var(--blue)"/>
    </svg>
    <span class="footer-date">12 May 2025</span><span class="footer-page">Page no: 06</span>
  </div>
</section>

<section class="slide slide--chart">
  <h2 class="slide-title">SIMPLE <span class="accent">CHART</span></h2>
  <div class="title-mark"></div>
  <div class="brand"><span class="brand-dot"></span><span class="brand-name">VARDUL</span></div>

  <div class="stat" style="left:13px;top:77px"><div class="stat-value">657</div><div class="stat-label">Excepteur sint</div></div>
  <div class="stat" style="left:13px;top:126px"><div class="stat-value">472</div><div class="stat-label stat-label--blue">Duis aute iruret</div></div>

  <svg class="chart" viewBox="0 0 250 115" width="250" height="115" role="img" aria-label="Bar chart of values F1 to F6">
    <g fill="var(--bar-blue)">
      <rect x="6" y="50" width="19" height="52"/>
      <rect x="40" y="32" width="19" height="70"/>
      <rect x="76" y="71" width="19" height="31"/>
      <rect x="111" y="66" width="19" height="36"/>
      <rect x="145" y="31" width="19" height="71"/>
    </g>
    <rect x="181" y="6" width="19" height="96" fill="var(--ink)"/>
    <line x1="0" y1="102.5" x2="208" y2="102.5" stroke="#d0d0d0" stroke-width="1"/>
    <g font-family="Montserrat, sans-serif" font-size="5.6" font-weight="600" fill="var(--blue)" text-anchor="middle">
      <text x="15.5" y="112">F1</text><text x="49.5" y="112">F2</text><text x="85.5" y="112">F3</text>
      <text x="120.5" y="112">F4</text><text x="154.5" y="112">F5</text><text x="190.5" y="112">F6</text>
    </g>
  </svg>

  <p class="chart-caption">Excepteur sint occaecat cupidatat non proident, sunt in culpa qui officia deserunt mollit anim id est laborum.</p>
  <div class="chart-notes">
    <p>Duis aute irure dolor in reprehenderit in voluptate velit esse cillum dolore eu fugiat nulla pariatur.</p>
    <p>Excepteur sint occaecat cupidatat non proident, sunt in culpa qui officia deserunt mollit anim id est laborum.</p>
  </div>

  <div class="footer">
    <svg viewBox="0 0 455 22" width="455" height="22" aria-hidden="true">
      <rect x="0" y="1" width="300" height="3" fill="var(--rule-grey)"/>
      <rect x="0" y="3" width="455" height="19" fill="var(--ink)"/>
      <path d="M278 22 C285 8 296 1 318 1 H455 V22 Z" fill="#d4d4d4"/>
      <path d="M283 22 C290 9 301 2 322 2 H455 V22 Z" fill="var(--blue)"/>
    </svg>
    <span class="footer-date">12 May 2025</span><span class="footer-page">Page no: 07</span>
  </div>
</section>

<section class="slide slide--contact">
  <div class="contact-watermark" aria-hidden="true"></div>
  <h2 class="slide-title">CONTACT <span class="accent">US</span></h2>
  <div class="title-mark"></div>
  <div class="contact-brand"><span class="contact-brand-dot"></span><span class="contact-brand-name">VARDUL</span></div>

  <div class="contact-item" style="left:22px">
    <span class="contact-icon"><svg viewBox="0 0 10 10" width="9" height="9" aria-hidden="true"><path d="M2.2 1 L3.6 2.6 L2.9 3.6 C3.4 4.8 4.9 6.4 6.3 7 L7.3 6.3 L9 7.7 L8.2 9 C4.6 8.8 1.1 5.3 1 1.8 Z" fill="#fff"/></svg></span>
    <div><p class="contact-label">CALL US</p><p class="contact-value">+64 2 71 38 52 16</p></div>
  </div>
  <div class="contact-item" style="left:157px">
    <span class="contact-icon"><svg viewBox="0 0 10 10" width="8" height="8" aria-hidden="true"><rect x="1" y="2.5" width="8" height="5.5" rx=".6" fill="#fff"/><path d="M1.3 2.8 L5 5.6 L8.7 2.8" stroke="var(--ink)" stroke-width=".8" fill="none"/></svg></span>
    <div><p class="contact-label">MAIL US</p><p class="contact-value">info@vardul.com</p></div>
  </div>
  <div class="contact-item" style="left:299px">
    <span class="contact-icon"><svg viewBox="0 0 10 10" width="9" height="9" aria-hidden="true"><path d="M5 9.3 C3 6.8 2 5.2 2 3.8 A3 3 0 0 1 8 3.8 C8 5.2 7 6.8 5 9.3 Z" fill="#fff"/><circle cx="5" cy="3.8" r="1.1" fill="var(--ink)"/></svg></span>
    <div><p class="contact-label">LOCATION</p><p class="contact-value">9 Tidewell Rise, Harbour Bay,<br>Northcove 0941</p></div>
  </div>

  <p class="thank-you">THANK YOU</p>

  <div class="footer">
    <svg viewBox="0 0 455 22" width="455" height="22" aria-hidden="true">
      <rect x="0" y="1" width="300" height="3" fill="var(--rule-grey)"/>
      <rect x="0" y="3" width="455" height="19" fill="var(--ink)"/>
      <path d="M278 22 C285 8 296 1 318 1 H455 V22 Z" fill="#d4d4d4"/>
      <path d="M283 22 C290 9 301 2 322 2 H455 V22 Z" fill="var(--blue)"/>
    </svg>
    <span class="footer-date">12 May 2025</span><span class="footer-page">Page no: 08</span>
  </div>
</section>

</body>
</html>
```